Business card for consulting firm

We need a double-sided business card for consulting firm, VantorQ. The card should be professional but also creative and visually interesting.

Target Market(s)

Engineering and technology; transport industries; safety critical / heavy industry.

Contact Information for Business Card

See attached file with details.

Font styles to use
Sans Serif

```html
<!DOCTYPE html>
<html lang="en">
<head>
<meta charset="utf-8">
<title>VantorQ Business Card</title>
<link href="https://fonts.googleapis.com/css2?family=Work+Sans:wght@400;500;600&display=swap" rel="stylesheet">
<style>
  :root {
    --navy: #0e2236;
    --cyan: #29abe2;
    --ink: #4a4f55;
    --mark-gray: #c9ccd0;
    --backdrop: #e6e8eb;
  }
  * { margin: 0; padding: 0; box-sizing: border-box; }
  html, body { width: 1200px; height: 900px; overflow: hidden; }
  body {
    background: var(--backdrop);
    font-family: "Work Sans", Arial, sans-serif;
    position: relative;
  }
  .card {
    position: absolute;
    left: 320px;
    width: 560px;
    height: 320px;
    border-radius: 18px;
    overflow: hidden;
    box-shadow: 0 6px 18px rgba(0,0,0,0.18);
  }
  .card-front { top: 100px; background: linear-gradient(160deg, #ffffff 40%, #f0f1f2 100%); }
  .card-back { top: 480px; background: var(--navy); display: flex; align-items: center; justify-content: center; }

  .brand-name {
    position: absolute;
    left: 40px;
    top: 36px;
    font-size: 46px;
    font-weight: 600;
    letter-spacing: 3px;
    color: var(--navy);
    white-space: nowrap;
  }
  .divider {
    position: absolute;
    left: 0;
    top: 186px;
    width: 440px;
    height: 1.5px;
    background: var(--cyan);
  }
  .person {
    position: absolute;
    right: 40px;
    top: 108px;
    text-align: right;
    white-space: nowrap;
  }
  .person-name {
    font-size: 24px;
    font-weight: 500;
    color: var(--cyan);
    letter-spacing: 0.5px;
  }
  .person-credentials {
    font-size: 10.5px;
    font-weight: 500;
    color: var(--navy);
    margin-top: 2px;
  }
  .person-role {
    font-size: 15px;
    color: var(--ink);
    margin-top: 3px;
    letter-spacing: 0.5px;
  }
  .contact-list {
    position: absolute;
    left: 34px;
    top: 202px;
    list-style: none;
  }
  .contact-list li {
    display: flex;
    align-items: center;
    gap: 9px;
    font-size: 13px;
    color: var(--ink);
    line-height: 21px;
    white-space: nowrap;
  }
  .contact-list svg { width: 10px; height: 10px; flex: none; }
  .web-caps {
    position: absolute;
    right: 110px;
    top: 244px;
    font-size: 17px;
    font-weight: 500;
    color: var(--cyan);
    letter-spacing: 0.5px;
    white-space: nowrap;
  }
  .bottom-tab {
    position: absolute;
    left: 250px;
    bottom: 0;
    width: 180px;
    height: 14px;
    background: var(--navy);
  }

  .back-mark {
    font-size: 64px;
    font-weight: 600;
    letter-spacing: 5px;
    color: var(--mark-gray);
  }
</style>
</head>
<body>
  <section class="card card-front" aria-label="Card front">
    <div class="brand-name">VANTORQ</div>

    <div class="person">
      <div class="person-name">HELENA MARSH</div>
      <div class="person-credentials">BEng (Hons), MBA, M Sys Eng (Safety)</div>
      <div class="person-role">Managing Director</div>
    </div>

    <div class="divider"></div>

    <ul class="contact-list">
      <li>
        <svg viewBox="0 0 10 10"><path d="M2 1 L4 1 L4.6 3 L3.4 3.8 Q4.4 5.8 6.2 6.6 L7 5.4 L9 6 L9 8 Q8.6 9 7.6 9 Q1 8.4 1 2.2 Q1.2 1 2 1Z" fill="var(--cyan)"/></svg>
        +61 (0)400 555 018
      </li>
      <li>
        <svg viewBox="0 0 10 10"><rect x="0.8" y="2" width="8.4" height="6" fill="none" stroke="var(--cyan)" stroke-width="1.2"/><path d="M1 2.4 L5 5.4 L9 2.4" fill="none" stroke="var(--cyan)" stroke-width="1.2"/></svg>
        hmarsh@vantorq.com.au
      </li>
      <li>
        <svg viewBox="0 0 10 10"><circle cx="5" cy="5" r="4.5" fill="var(--cyan)"/></svg>
        www.vantorq.global
      </li>
    </ul>

    <div class="web-caps">WWW.VANTORQ.COM.AU</div>
    <div class="bottom-tab"></div>
  </section>

  <section class="card card-back" aria-label="Card back">
    <div class="back-mark">VANTORQ</div>
  </section>
</body>
</html>
```